business card design for velmora textile printing

Velmora Textile Printing requires elegant and colorful designs for its business card, ensuring both are visually cohesive and reflect the brand’s creative, modern identity. The logo is already finalized and should be a central element in designs.

## Business Card Design Brief

- Feature the logo clearly, with colors and style matching the letterhead.
- Present contact information (name, title, phone, email, website, address) in a clear, organized manner.
- Open to creative layouts, finishes, and double-sided designs, as long as the card remains professional and easy to read.
- Ensure both pieces feel unified as part of the same brand identity.

The final designs should be vibrant, professional, and memorable, showcasing Velmora Textile Printing’s creative spirit.

Target Market(s)

Pakistan

Industry/Entity Type

Textile printing

Other font styles liked:
• Calibri

Requirements
Must have
• Address Email Address Phone number designer can ask me when start designing

```html
<!DOCTYPE html>
<html lang="en">
<head>
<meta charset="utf-8">
<title>Velmora Textile Printing — Business Card</title>
<link rel="stylesheet" href="https://fonts.googleapis.com/css2?family=Montserrat:wght@500;600;700&display=swap">
<style>
  :root {
    --page-bg: #3a3a3c;
    --card-white: #ffffff;
    --card-black: #1b1b1b;
    --brand-orange: #f47a12;
    --brand-magenta: #c81d8f;
    --ink-dark: #1f1f1f;
    --logo-maroon: #4a1c22;
    --logo-cream: #f6efdc;
  }
  * { box-sizing: border-box; margin: 0; padding: 0; }
  html, body {
    width: 1200px; height: 1200px; overflow: hidden;
    background: var(--page-bg);
    font-family: "Montserrat", sans-serif;
  }
  .sheet {
    width: 1200px; height: 1200px;
    display: flex; flex-direction: column; align-items: center; justify-content: center;
    gap: 32px;
  }
  .card {
    position: relative;
    width: 960px; height: 549px;
    border-radius: 40px;
    overflow: hidden;
  }
  .card--front { background: var(--card-white); }
  .card--back { background: var(--card-black); display: flex; align-items: center; justify-content: center; }

  .card__wave { position: absolute; inset: 0; width: 100%; height: 100%; }

  .contact {
    position: absolute; left: 72px; top: 150px;
    color: var(--ink-dark);
  }
  .contact__name {
    font-size: 46px; font-weight: 700; color: var(--brand-orange);
    letter-spacing: 0.5px; line-height: 1;
  }
  .contact__role {
    font-size: 24px; font-weight: 500; margin-top: 6px; letter-spacing: 0.5px;
  }
  .contact__list { list-style: none; margin-top: 22px; }
  .contact__item {
    display: flex; align-items: flex-start; gap: 14px;
    font-size: 21px; font-weight: 500; line-height: 1.25; margin-bottom: 8px;
  }
  .contact__icon { width: 24px; height: 24px; flex: none; margin-top: 2px; }

  .brand {
    display: flex; align-items: center; gap: 16px;
  }
  .brand--front { position: absolute; right: 90px; top: 150px; }
  .brand__dot {
    width: 40px; height: 40px; border-radius: 50%;
    background: var(--brand-orange); flex: none;
  }
  .brand__name {
    font-weight: 700; font-size: 34px; line-height: 1.1; letter-spacing: 1px;
    text-transform: uppercase;
  }
  .brand--front .brand__name { color: var(--logo-maroon); }
  .brand--back .brand__name { color: var(--logo-cream); font-size: 44px; }
  .brand--back .brand__dot { width: 52px; height: 52px; }
</style>
</head>
<body>
<main class="sheet">

  <section class="card card--front" aria-label="Business card front">
    <svg class="card__wave" viewBox="0 0 960 549" preserveAspectRatio="none" aria-hidden="true">
      <defs>
        <linearGradient id="waveAccent" x1="0" y1="1" x2="1" y2="0">
          <stop offset="0" stop-color="#f47a12"/>
          <stop offset="0.55" stop-color="#e64a5c"/>
          <stop offset="1" stop-color="#c81d8f"/>
        </linearGradient>
      </defs>
      <path d="M205,549 C360,400 660,455 800,360 C880,305 925,270 960,232 L960,549 Z" fill="url(#waveAccent)"/>
      <path d="M228,549 C380,418 670,470 810,376 C885,324 930,288 960,260 L960,549 Z" fill="#ffffff"/>
      <path d="M246,549 C395,432 680,482 818,390 C890,340 933,304 960,280 L960,549 Z" fill="#1b1b1b"/>
    </svg>

    <div class="contact">
      <h1 class="contact__name">FULL NAME</h1>
      <p class="contact__role">POSITION</p>
      <ul class="contact__list">
        <li class="contact__item">
          <svg class="contact__icon" viewBox="0 0 24 24" aria-hidden="true"><path fill="#f47a12" d="M6.6 10.8a15.1 15.1 0 0 0 6.6 6.6l2.2-2.2c.3-.3.7-.4 1-.2 1.1.4 2.3.6 3.6.6.6 0 1 .4 1 1V20c0 .6-.4 1-1 1A17 17 0 0 1 3 4c0-.6.4-1 1-1h3.5c.6 0 1 .4 1 1 0 1.3.2 2.5.6 3.6.1.3 0 .7-.2 1z"/></svg>
          <span>(000) 000 0000</span>
        </li>
        <li class="contact__item">
          <svg class="contact__icon" viewBox="0 0 24 24" aria-hidden="true"><path fill="#f47a12" d="M2 5h20v14H2z"/><path fill="none" stroke="#fff" stroke-width="1.8" d="M2.5 5.5 12 13l9.5-7.5"/></svg>
          <span>email@company.com</span>
        </li>
        <li class="contact__item">
          <svg class="contact__icon" viewBox="0 0 24 24" aria-hidden="true"><g fill="none" stroke="#f47a12" stroke-width="1.8"><circle cx="12" cy="12" r="9.5"/><ellipse cx="12" cy="12" rx="4.5" ry="9.5"/><path d="M2.5 12h19M4 7h16M4 17h16"/></g></svg>
          <span>www.company.com</span>
        </li>
        <li class="contact__item">
          <svg class="contact__icon" viewBox="0 0 24 24" aria-hidden="true"><path fill="#f47a12" d="M12 2a7 7 0 0 0-7 7c0 5.2 7 13 7 13s7-7.8 7-13a7 7 0 0 0-7-7zm0 9.5A2.5 2.5 0 1 1 12 6.5a2.5 2.5 0 0 1 0 5z"/></svg>
          <span>123 Name Street, 000<br>Your City, 00000-000</span>
        </li>
      </ul>
    </div>

    <div class="brand brand--front">
      <span class="brand__dot" aria-hidden="true"></span>
      <span class="brand__name">Velmora<br>Textile Printing</span>
    </div>
  </section>

  <section class="card card--back" aria-label="Business card back">
    <div class="brand brand--back">
      <span class="brand__dot" aria-hidden="true"></span>
      <span class="brand__name">Velmora<br>Textile Printing</span>
    </div>
  </section>

</main>
</body>
</html>
```